Web design for a relaunch of a technology and knowledge transfer company

Design for the relaunch of an existing website The company specializes in technology and knowledge transfer between companies (and universities). The innovation company (company name) combines many years of experience in technology transfer, innovation management, project management and grant applications. Link: http://www.vorlaufwerkstatt.example The colors of the logo are not very advantageous and can be adjusted a bit. There are currently no picture worlds, these are to be selected by the designer. Abstract motifs are certainly an advantage here (10 motifs). Animated programming could be done (network etc. http://pelvart.qmstudio.example/). In this case a suggestion is made, which we convert programming technically. The structure and contents of the existing pages will be adopted and supplemented. The programming will be done with TYPO3 in responsive form (bootstrap). Required are start page, content page and contact page. -------------------------------------------------- ------------------------------ Web design for a relaunch of a company in technology and knowledge transfer Design for the relaunch of an existing website. The company specializes in technology and knowledge transfer between companies (and universities). The innovation company combines many years of experience in the fields of technology transfer, innovation management, project management and grant application. Link: http://www.vorlaufwerkstatt.example The color of the logo is not exactly advantageous and can be adjusted. There are currently no image worlds, these are to be selected by the designer. Abstract motifs are certainly an advantage here (10 motifs). It could also be made animated programming (network, etc. http://pelvart.qmstudio.example/). In this case, a proposal has to be made, which we implement in terms of programming technology. The structure and contents of the existing pages are taken over and supplemented. Programming is done with TYPO3 in responsive form (bootstrap). Required are homepage, content page and contact page.

```html
<!DOCTYPE html>
<html lang="en">
<head>
<meta charset="utf-8">
<title>Vorlaufwerkstatt – Technology and Knowledge Transfer</title>
<link href="https://fonts.googleapis.com/css2?family=Poppins:wght@400;500;600;700&display=swap" rel="stylesheet">
<style>
  :root {
    --brand-blue: #1a1f9e;
    --royal-blue: #1c2ea6;
    --signal-red: #e31937;
    --ink: #2b2b2b;
    --muted: #8a8a8a;
    --white: #ffffff;
    --footer-bg: #1f272e;
    --footer-text: #c9cdd2;
  }
  * { margin: 0; padding: 0; box-sizing: border-box; }
  html, body { width: 1200px; height: 2528px; overflow: hidden; }
  body { position: relative; font-family: "Poppins", sans-serif; color: var(--ink); background: var(--white); }
  .abs { position: absolute; }

  /* Header */
  .site-header { left: 0; top: 0; width: 1200px; height: 80px; background: var(--white); }
  .brand { left: 121px; top: 18px; display: flex; align-items: center; gap: 12px; }
  .brand-mark { width: 40px; height: 40px; background: var(--brand-blue); }
  .brand-name { font-size: 21px; font-weight: 500; color: var(--brand-blue); }
  .main-nav a { position: absolute; top: 31px; font-size: 12px; font-weight: 500; color: var(--ink); text-decoration: none; white-space: nowrap; }
  .main-nav a.is-active { color: var(--brand-blue); }
  .search-icon { left: 1062px; top: 30px; }

  /* Hero */
  .hero { left: 0; top: 80px; width: 1200px; height: 640px;
    background: radial-gradient(ellipse at 35% 40%, #4f86b4 0%, #1f4f78 40%, #0f2d4d 75%, #0b2440 100%); }
  .hero-frame { left: 652px; top: 190px; width: 351px; height: 401px; border: 1px solid #ffffff; }
  .hero-frame-inner { left: 652px; top: 190px; width: 351px; height: 401px; border-right: 1px solid var(--signal-red); border-bottom: 1px solid var(--signal-red); }
  .hero-card { left: 674px; top: 212px; width: 349px; height: 400px; background: var(--white); }
  .hero-title { left: 725px; top: 258px; width: 280px; font-size: 29px; line-height: 35px; font-weight: 600; color: var(--brand-blue); }
  .hero-lead { left: 725px; top: 447px; width: 240px; font-size: 14px; line-height: 23px; color: var(--muted); }
  .btn { display: flex; align-items: center; justify-content: center; font-size: 11.5px; font-weight: 600; text-decoration: none; white-space: nowrap; }
  .btn-red { background: var(--signal-red); color: var(--white); }
  .btn-white { background: var(--white); color: var(--signal-red); }
  .hero-btn { left: 725px; top: 573px; width: 158px; height: 39px; }

  /* About */
  .about { left: 0; top: 720px; width: 725px; height: 480px; background: var(--signal-red); }
  .about-title { left: 121px; top: 780px; width: 445px; font-size: 20.5px; line-height: 23.5px; font-weight: 600; color: var(--white); hyphens: auto; -webkit-hyphens: auto; }
  .about-text { left: 121px; top: 918px; width: 395px; font-size: 11.5px; line-height: 19px; color: var(--white); }
  .about-rule { left: 121px; top: 1035px; width: 463px; height: 1px; background: rgba(255,255,255,.75); }
  .about-note { left: 121px; top: 1062px; width: 290px; font-size: 14.5px; line-height: 21px; font-weight: 500; color: var(--white); }
  .about-btn { left: 121px; top: 1161px; width: 191px; height: 39px; }
  .about-photo { left: 615px; top: 821px; width: 465px; height: 279px; border-radius: 9px;
    background: linear-gradient(120deg, #6f7a5c 0%, #a7a093 40%, #c9c2b8 60%, #3b3530 100%);
    box-shadow: 0 20px 40px rgba(0,0,0,.18); }

  /* Services */
  .section-title { width: 1200px; left: 0; text-align: center; font-weight: 600; }
  .services-title { top: 1256px; font-size: 28px; color: var(--brand-blue); }
  .service-side { top: 1392px; height: 302px; border-radius: 9px; }
  .service-left { left: 244px; width: 140px; background: linear-gradient(135deg, #f2f2f2, #c4c4c4 60%, #8d8d8d); }
  .service-right { left: 816px; width: 140px; background: linear-gradient(135deg, #0d2038, #20486e 55%, #0b1626); }
  .service-main { left: 369px; top: 1351px; width: 462px; height: 381px; border-radius: 10px;
    background: linear-gradient(140deg, #d7d7d7 0%, #8c8c8c 35%, #5b5b5b 60%, #b0b0b0 100%);
    box-shadow: 0 25px 45px rgba(0,0,0,.28); }
  .service-title { left: 408px; top: 1566px; width: 310px; font-size: 20px; line-height: 23px; font-weight: 600; color: var(--white); }
  .service-text { left: 408px; top: 1624px; width: 360px; font-size: 11px; line-height: 14px; color: var(--white); }
  .service-btn { left: 408px; top: 1695px; width: 111px; height: 37px; }

  /* Reports */
  .reports { left: 0; top: 1808px; width: 1200px; height: 479px; background: var(--royal-blue); }
  .reports-title { top: 1864px; font-size: 29px; color: var(--white); }
  .report { top: 1960px; width: 216px; }
  .report-photo { width: 216px; height: 135px; border-radius: 8px; }
  .report-date { margin-top: 14px; font-size: 11px; color: var(--signal-red); }
  .report-title { margin-top: 6px; width: 195px; font-size: 13.5px; line-height: 17px; font-weight: 600; color: var(--white); hyphens: auto; -webkit-hyphens: auto; }
  .report-title.is-linked { text-decoration: underline; }

  /* Footer */
  .site-footer { left: 0; top: 2287px; width: 1200px; height: 241px; background: var(--footer-bg); }
  .footer-nav a { position: absolute; top: 2385px; font-size: 12px; color: var(--footer-text); text-decoration: none; white-space: nowrap; }
  .copyright { left: 167px; top: 2413px; font-size: 12px; color: var(--footer-text); }
  .social { top: 2389px; width: 34px; height: 34px; border-radius: 50%; background: #c9cdd2; }
</style>
</head>
<body>

<header class="site-header abs">
  <div class="brand abs"><span class="brand-mark"></span><span class="brand-name">Vorlaufwerkstatt</span></div>
  <nav class="main-nav">
    <a href="#" class="is-active" style="left:622px">Services</a>
    <a href="#" style="left:704px">References</a>
    <a href="#" style="left:802px">Workshops</a>
    <a href="#" style="left:901px">Reports</a>
    <a href="#" style="left:980px">Contact</a>
  </nav>
  <svg class="search-icon abs" width="16" height="16" viewBox="0 0 16 16" fill="none" stroke="#2b2b2b" stroke-width="1.5">
    <circle cx="9.5" cy="6.5" r="5"/><line x1="6" y1="10" x2="1.5" y2="14.5"/>
  </svg>
</header>

<section class="hero abs" role="img" aria-label="Hand touching glowing gears above two light bulbs on a dark blue background"></section>
<div class="hero-frame abs"></div>
<div class="hero-card abs"></div>
<div class="hero-frame-inner abs"></div>
<h1 class="hero-title abs">We Specializes in technology and knowledge transfer between companies</h1>
<p class="hero-lead abs">that supports companies in implementing their innovative ideas.</p>
<a href="#" class="btn btn-red hero-btn abs">Explore More</a>

<section class="about abs"></section>
<h2 class="about-title abs">The innovation company brings together over 15 years of experience in the areas of technology transfer, innovation management, project management and grant application.</h2>
<p class="about-text abs">Lorem ipsum dolor sit amet, consectetur adipiscing elit, eiusmod tempor incididunt ut labore et dolore magna aliqua. Ut enim ad minim veniam, quis nostrud exercitation ullamco laboris nisi ut aliquip ex ea commodo consequat.</p>
<div class="about-rule abs"></div>
<p class="about-note abs">Together we will find the right answers for you and your company!</p>
<a href="#" class="btn btn-white about-btn abs">Contact Us Today!</a>
<div class="about-photo abs" role="img" aria-label="Woman writing notes at a desk in a bright office"></div>

<h2 class="section-title services-title abs">Services We Offer</h2>
<div class="service-side service-left abs" role="img" aria-label="Chrome spheres of a molecular model"></div>
<div class="service-side service-right abs" role="img" aria-label="Abstract dark blue digital network"></div>
<div class="service-main abs" role="img" aria-label="Close-up of metal gear wheels"></div>
<h3 class="service-title abs">Technology and knowledge transfer</h3>
<p class="service-text abs">The innovation society is a technology and knowledge transfer company that supports companies in implementing their innovative ideas.</p>
<a href="#" class="btn btn-white service-btn abs">Learn More</a>

<section class="reports abs"></section>
<h2 class="section-title reports-title abs">Reports on Current Topics and Events</h2>
<article class="report abs" style="left:120px">
  <div class="report-photo" role="img" aria-label="Speaker presenting in a lecture hall" style="background:linear-gradient(135deg,#6b5a45,#a89a86 55%,#3d342b)"></div>
  <p class="report-date">09. 10. 2018</p>
  <h3 class="report-title" style="width:175px">IoT - what companies want</h3>
</article>
<article class="report abs" style="left:367px">
  <div class="report-photo" role="img" aria-label="Group of people talking at a conference" style="background:linear-gradient(135deg,#2d3e5c,#8e97a6 50%,#e6e4e0)"></div>
  <p class="report-date">09. 10. 2018</p>
  <h3 class="report-title is-linked">StartLab Conference on the 5th and 6th of September in Minden</h3>
</article>
<article class="report abs" style="left:615px">
  <div class="report-photo" role="img" aria-label="Two men in conversation in a laboratory hall" style="background:linear-gradient(135deg,#c7c9cb,#6f6a63 50%,#2c2a28)"></div>
  <p class="report-date">02. 31. 2018</p>
  <h3 class="report-title">In conversation with the Halvorsen Institut Lemgo</h3>
</article>
<article class="report abs" style="left:863px">
  <div class="report-photo" role="img" aria-label="Group portrait of a team standing together" style="background:linear-gradient(135deg,#8a7e72,#3a3836 55%,#b7aea4)"></div>
  <p class="report-date">02. 14. 2018</p>
  <h3 class="report-title">Engagement intensified</h3>
</article>

<footer class="site-footer abs"></footer>
<nav class="footer-nav">
  <a href="#" style="left:167px">Services</a>
  <a href="#" style="left:256px">References</a>
  <a href="#" style="left:362px">Workshops</a>
  <a href="#" style="left:467px">Reports</a>
  <a href="#" style="left:553px">Contact</a>
</nav>
<p class="copyright abs">© 2019. Vorlaufwerkstatt</p>
<span class="social abs" style="left:831px"></span>
<span class="social abs" style="left:873px"></span>
<span class="social abs" style="left:915px"></span>
<span class="social abs" style="left:957px"></span>
<span class="social abs" style="left:999px"></span>

</body>
</html>
```